Historic Church website

We want our church website to feel warm, historic, and clean, modern, and easy to navigate. Dont use the anchor

Current website: https://www.meadowlarkfellowship.org/

Requirements
Should not have
• I would like to use the logo without the anchor

```html
<!DOCTYPE html>
<html lang="en">
<head>
<meta charset="utf-8">
<title>Meadowlark Fellowship Church</title>
<link href="https://fonts.googleapis.com/css2?family=Rubik:wght@400;500;700&family=Montserrat:wght@400;500;600;700&display=swap" rel="stylesheet">
<style>
:root{
  --ink:#141110;
  --ink-2:#1c1815;
  --ink-3:#241d18;
  --gold:#c9974a;
  --gold-light:#e2bd7a;
  --gold-dark:#8d6428;
  --cream:#f1e6d2;
  --text:#e9e2d6;
  --muted:#b8ab98;
  --parch-1:#c9a86e;
  --parch-2:#a57f45;
}
*{box-sizing:border-box;margin:0;padding:0}
html,body{width:1200px;height:3908px;overflow:hidden}
body{background:var(--ink);color:var(--text);font-family:"Montserrat",sans-serif;position:relative}
.head-font{font-family:"Rubik",sans-serif}
.btn{display:inline-block;background:linear-gradient(180deg,var(--gold-light),var(--gold) 55%,var(--gold-dark));color:#2a1c0a;font:600 11px "Montserrat",sans-serif;letter-spacing:1px;text-transform:uppercase;padding:11px 22px;border-radius:2px;text-decoration:none}
.rule{position:absolute;left:0;width:1200px;height:3px;background:linear-gradient(90deg,transparent,var(--gold) 20%,var(--gold-light) 50%,var(--gold) 80%,transparent)}
section{position:absolute;left:0;width:1200px;overflow:hidden}
.photo{position:absolute}

/* hero */
.hero{top:0;height:920px}
.hero .photo{inset:0;background:radial-gradient(ellipse at 50% 70%,#7a4a22 0%,#3a2515 35%,#1a120d 75%),#1a120d}
.hero .shade{position:absolute;inset:0;background:linear-gradient(180deg,rgba(10,8,6,.75),rgba(10,8,6,.15) 45%,rgba(10,8,6,.55))}
.nav{position:absolute;top:22px;left:230px;right:230px;display:flex;align-items:center;justify-content:space-between}
.brand{display:flex;align-items:center;gap:12px;font:500 20px "Rubik",sans-serif;color:var(--cream)}
.brand-dot{width:34px;height:34px;border-radius:50%;background:var(--cream)}
.menu{display:flex;align-items:center;gap:26px;font:600 11px "Montserrat",sans-serif;letter-spacing:.8px;text-transform:uppercase;color:var(--cream)}
.menu .donate{border:1px solid var(--cream);padding:10px 16px}
.hero-copy{position:absolute;top:225px;left:0;width:1200px;text-align:center}
.hero-copy .l1{font:400 50px "Rubik",sans-serif;color:var(--gold);letter-spacing:1px}
.hero-copy .l2{font:700 52px "Rubik",sans-serif;color:#fff;letter-spacing:1px;margin-top:6px}
.hero-copy .sub{font:600 15px "Montserrat",sans-serif;color:var(--cream);letter-spacing:.8px;text-transform:uppercase;margin-top:26px}
.hero-copy .btn{margin-top:40px}

/* features */
.features{top:920px;height:380px;background:linear-gradient(180deg,#1d1916,#151210)}
.feature{position:absolute;top:92px;width:260px;text-align:center}
.feature svg{width:56px;height:56px}
.feature h3{font:500 18px "Rubik",sans-serif;color:var(--gold);text-transform:uppercase;letter-spacing:1px;margin-top:12px}
.feature p{font-size:12px;line-height:1.6;color:var(--muted);margin:12px auto 0;width:210px}
.feature .btn{margin-top:30px;padding:9px 18px;font-size:10px}

/* about */
.about{top:1303px;height:660px}
.about .photo{inset:0;background:radial-gradient(ellipse at 85% 55%,#6b4322 0%,#2f2015 35%,#16110d 70%)}
.about h2{position:absolute;top:60px;left:140px;font:400 38px "Rubik",sans-serif;color:var(--gold);line-height:1.2}
.about h2 b{display:block;font-weight:700;color:#fff}
.about p{position:absolute;top:200px;left:440px;width:560px;font-size:12px;line-height:1.85;color:var(--text)}

/* service */
.service{top:1966px;height:364px;background:linear-gradient(180deg,#1c1714,#141110);text-align:center}
.service h2{margin-top:62px;font:400 38px "Rubik",sans-serif;color:var(--gold)}
.service h2 b{color:#fff;font-weight:700}
.sub-label{display:inline-block;margin-top:12px;font:600 13px "Montserrat",sans-serif;letter-spacing:1.2px;color:var(--cream);text-transform:uppercase;border-top:1px solid var(--gold);border-bottom:1px solid var(--gold);padding:5px 30px}
.service p{font-size:12px;line-height:1.7;color:var(--muted);margin-top:26px}
.service .btn{margin-top:28px}

/* events */
.events{top:2330px;height:770px;text-align:center}
.events .photo{inset:0;background:radial-gradient(ellipse at 90% 50%,#5a3a1e 0%,#271a12 35%,#15110e 70%)}
.events .inner{position:relative}
.events h2{margin-top:62px;font:400 38px "Rubik",sans-serif;color:var(--gold)}
.events h2 b{color:#fff;font-weight:700}
.card{position:absolute;top:160px;width:190px;text-align:left}
.card .thumb{height:170px;border:2px solid var(--gold-dark);background:linear-gradient(160deg,#6a4526,#2e1f14)}
.card p{font-size:11px;line-height:1.55;color:var(--text);margin-top:14px}
.events .btn{position:absolute;top:518px;left:535px}

/* quote */
.quote{top:3100px;left:240px;width:720px;height:220px;background:radial-gradient(ellipse at 50% 50%,var(--parch-1),var(--parch-2));text-align:center;color:#1c130a;padding:38px 50px}
.quote blockquote{font:700 17px "Montserrat",sans-serif;line-height:1.45;font-style:normal}
.quote cite{display:block;margin-top:22px;font:700 24px "Rubik",sans-serif;font-style:normal;letter-spacing:.5px}

/* footer */
.footer{top:3320px;height:588px;background:var(--ink)}
.footer .cols{position:absolute;top:28px;left:140px;right:140px;height:460px}
.col{position:absolute;top:0;font-size:11px;line-height:1.75;color:var(--text)}
.col h4{font:500 14px "Rubik",sans-serif;color:var(--gold);margin-bottom:10px}
.col .gap{margin-top:14px}
.footer .bottom{position:absolute;top:500px;left:140px;right:140px;border-top:1px solid #3a302a;padding-top:18px;font-size:10px;color:var(--muted);display:flex;justify-content:center;gap:20px}
.footer .bottom span:last-child{position:absolute;right:0}
</style>
</head>
<body>

<section class="hero">
  <div class="photo" role="img" aria-label="Warm historic library lounge with leather armchairs and a lit fireplace"></div>
  <div class="shade"></div>
  <nav class="nav">
    <div class="brand"><span class="brand-dot"></span>Meadowlark Fellowship Church</div>
    <div class="menu">
      <span>About MFC</span><span>Ministries</span><span>Bible Studies</span><span>Sermon Library</span><span class="donate">Donate Now</span>
    </div>
  </nav>
  <div class="hero-copy">
    <div class="l1">ROOTED IN ANCIENT FAITH.</div>
    <div class="l2">GUIDED BY ETERNAL TRUTH.</div>
    <div class="sub">Rooted in historic Christianity. Shaped by Scripture, and faithfully</div>
    <a class="btn" href="#">Join our community &rarr;</a>
  </div>
</section>

<div class="rule" style="top:918px"></div>

<section class="features">
  <div class="feature" style="left:210px">
    <svg viewBox="0 0 56 56" fill="none" stroke="#c9974a" stroke-width="2.5"><circle cx="28" cy="28" r="22"/><circle cx="28" cy="28" r="13"/><circle cx="28" cy="28" r="4" fill="#c9974a"/><path d="M28 28 46 10M40 10h6v6"/></svg>
    <h3>Our Mission</h3>
    <p>MFC exists to glorify the Triune God and make disciples of Jesus Christ.</p>
    <a class="btn" href="#">Learn More &rarr;</a>
  </div>
  <div class="feature" style="left:470px">
    <svg viewBox="0 0 56 56" fill="none" stroke="#c9974a" stroke-width="2.5"><path d="M10 34v-6a18 18 0 0 1 36 0v6"/><rect x="7" y="32" width="9" height="15" rx="3"/><rect x="40" y="32" width="9" height="15" rx="3"/></svg>
    <h3>Listen to Sermons</h3>
    <p>A New Song for a Renewed World<br>January 11, 2026</p>
    <a class="btn" href="#">Learn More &rarr;</a>
  </div>
  <div class="feature" style="left:730px">
    <svg viewBox="0 0 56 56" fill="none" stroke="#c9974a" stroke-width="2.5"><circle cx="28" cy="28" r="19"/><circle cx="28" cy="9" r="5" fill="#141110"/><circle cx="11" cy="38" r="5" fill="#141110"/><circle cx="45" cy="38" r="5" fill="#141110"/></svg>
    <h3>Get Connected</h3>
    <p>Get Connected with our Meadowlark Fellowship Church</p>
    <a class="btn" href="#">Learn More &rarr;</a>
  </div>
</section>

<div class="rule" style="top:1300px"></div>

<section class="about">
  <div class="photo" role="img" aria-label="Dim study with bookshelves, a lit candle and a globe"></div>
  <h2>MEADOWLARK FELLOWSHIP CHURCH IS AN<b>INDEPENDENT CHRISTIAN CHURCH<br>IN THE PROTESTANT TRADITION.</b></h2>
  <p>As central tenets are found in its Articles of Faith and include belief in the Deity and Lordship of Jesus Christ, the Trinity, Jesus' perfect life, atoning death on the cross, bodily resurrection, and ascension. Jesus' literal return; the inerrancy of the Bible in its original manuscripts; and our need for salvation through personal faith in Jesus Christ. In keeping with the prevailing perspective of the church during the centuries immediately following the Apostles, we teach Premillennialism. That is, the belief that Messiah will physically and literally return to earth at Jerusalem before the millennial age commences. At that time, he will establish a kingdom over which he will preside as King. All the promises of Israel's covenants will be literally fulfilled during this reign. At the end of one thousand years, the kingdom will be transferred from the Son to the Father and will merge with the eternal kingdom.</p>
</section>

<div class="rule" style="top:1963px"></div>

<section class="service">
  <h2>JOIN US <b>THIS SUNDAY</b></h2>
  <div class="sub-label">Workshop Services</div>
  <p>Sunday Morning Worship Service 11:00 AM – 12:45 PM<br>Sunday worship and service take place in the main sanctuary.</p>
  <a class="btn" href="#">Plan to visit &rarr;</a>
</section>

<section class="events">
  <div class="photo" role="img" aria-label="Old library with wooden shelves and a brass globe"></div>
  <div class="inner">
    <h2>UPCOMING <b>MFC EVENTS</b></h2>
    <div class="sub-label">Latest Programs</div>
    <div class="card" style="left:250px">
      <div class="thumb" role="img" aria-label="Reading room with bookshelves and a lamp"></div>
      <p>Where is MFC?<br>We are on the northeast corner of Larkspur Ave and Elm Street in Fairhaven. The entrance is on Larkspur Ave.</p>
    </div>
    <div class="card" style="left:470px">
      <div class="thumb" role="img" aria-label="Wood panelled study with shelves of books"></div>
      <p>Join us for our mid-week Bible Study from 7:00 to 8:15pm. Meets at MFC. Contact church office for details.</p>
    </div>
    <div class="card" style="left:690px">
      <div class="thumb" role="img" aria-label="Historic library hall with tall bookcases"></div>
      <p>Where is MFC?<br>We are on the northeast corner of Larkspur Ave and Elm Street in Fairhaven. The entrance is on Larkspur Ave.</p>
    </div>
    <a class="btn" href="#">View all events &rarr;</a>
  </div>
</section>

<section class="quote" role="group">
  <blockquote>“Christians are called to God’s service not only in church professions but also in every secular calling. The task of restoring truth to the culture depends largely on our laypeople.”</blockquote>
  <cite>J. HARLAN WHITCOMBE</cite>
</section>

<footer class="footer" style="position:absolute;left:0;width:1200px">
  <div class="cols">
    <div class="col" style="left:0">
      <h4>Contact Us</h4>
      2200 Larkspur Avenue<br>Fairhaven, Oregon 97400<br>Phone: 541.555.0142<br>Email: info@meadowlarkfellowship.org
    </div>
    <div class="col" style="left:340px">
      <h4>Sermons</h4>
      A New Song for a Renewed World<br>January 11, 2026<br>Meadowlark Fellowship Church
      <div class="gap">The Lion and the Lamb Reigns<br>January 4, 2026<br>Meadowlark Fellowship Church</div>
      <div class="gap">The Kingdom is Coming<br>December 28, 2025<br>Meadowlark Fellowship Church</div>
    </div>
    <div class="col" style="left:600px">
      <h4>Quick Links</h4>
      Home<br>Who We Are<br>Visiting on a Sunday<br>Kids Church<br>Event Calendar<br>Our Ministries<br>Sunday Bible Studies<br>Sermons<br>Contact Us<br>Donate
    </div>
    <div class="col" style="left:810px">
      <h4>Social Media</h4>
      Community Page<br>Photo Stream<br>Video Channel<br>News Feed
    </div>
  </div>
  <div class="bottom">
    <span>© Copyright 2026 | Meadowlark Fellowship Church, Fairhaven, Oregon | All Rights Reserved.</span>
    <span>&uarr;</span>
  </div>
</footer>

</body>
</html>
```